依頼詳細
ホテル内レストランなので、高級感ラグジュアリー感のあるデザイン希望

ターゲット:ホテルご宿泊者様向け

・ディナーご利用時1ドリンクサービス
・カラオケ個室完備
・パーティー
記載項目
社名:株式会社ミルトフォレスト
店舗名:KAEDE NOGIZAKAA
住所: 〒107-0061 東京都港区北青山5-27-9アパホテル&リゾート〈六本木駅東〉1階
TEL/FAX 03-6781-2294
サイズ
A6
ページ数
片面
希望イメージ
シンプル 複雑
単色 カラフル
暗い 明るい
日常 高級
遊び心 厳粛
未来的 伝統的
女性的 男性的
希望する色
設定なし
納品ファイル
• 高解像度JPG (.jpg)
• イラストレーター形式 (.ai)
• PNG形式 (.png)
補足説明
本コンペ入選者でランチ半額のチラシを依頼したく思っております。よろしくお願いします。
記載いただきたい内容の文言追記します。
写真も店内写真とビュッフェ写真を追加します。よろしくお願いいたします。

・パーティー
→3,000円/ブッフェ+free drink

→5,000円/ブッフェ+freedrink

→1万円/ブッフェ+freedrink

※貸切
・30名以上/15万円以上/2時間
追加料金→30分..1万円/1時間..2万円

・カラオケ→1時間..大7,000円/小5,000円

※予算・内容に応じてご予約承ります。
■ 選んだ理由

コンセプトのマッチと表現方法、今後展開したいイメージにあっているため、選ばせていただきました。チラシをぱっとみて、何を伝えたいのかが読み取りやすい構成が素晴らしいと感じました。

■ 提案者全員のお礼・コメント

今回たくさんの方にご提案いただき本当にありがとうございました。弊社複数の事業展開をしており、
新店もぞくぞくオープンしていくので、広告需要が高いです。今後ともみなさまからのご提案を何卒よろしくお願いいたします!

```html
<!DOCTYPE html>
<html lang="ja">
<head>
<meta charset="utf-8">
<title>各種パーティー承ります｜KAEDE NOGIZAKAA</title>
<link rel="stylesheet" href="https://fonts.googleapis.com/css2?family=Noto+Serif+JP:wght@500;700;900&family=Noto+Sans+JP:wght@400;500;700&display=swap">
<style>
:root{
  --paper:#fdfaf3;
  --gold-deep:#a8781f;
  --gold:#d4a84a;
  --gold-light:#f3dc9c;
  --gold-pale:#fbf0d2;
  --brown:#6a4a1e;
  --ink:#2a2118;
  --ink-soft:#4a3d30;
}
*{margin:0;padding:0;box-sizing:border-box}
html,body{width:848px;height:1200px;overflow:hidden;background:var(--paper)}
.flyer{position:relative;width:848px;height:1200px;overflow:hidden;
  background:var(--paper);font-family:"Noto Sans JP",sans-serif;color:var(--ink)}
.glitter{position:absolute;border-radius:50%;filter:blur(6px)}
.glitter--top{left:-200px;top:-220px;width:760px;height:520px;
  background:radial-gradient(ellipse at 40% 40%,var(--gold-light) 0%,var(--gold) 40%,rgba(212,168,74,0) 72%);opacity:.85}
.glitter--right{right:-260px;top:120px;width:460px;height:900px;
  background:radial-gradient(ellipse at 50% 50%,var(--gold-pale) 0%,var(--gold) 45%,rgba(212,168,74,0) 72%);opacity:.7}
.glitter--bottom{left:-220px;bottom:-240px;width:880px;height:520px;
  background:radial-gradient(ellipse at 50% 55%,var(--gold-light) 0%,var(--gold) 40%,rgba(212,168,74,0) 72%);opacity:.9}
.frame{position:absolute;left:34px;top:34px;right:34px;bottom:34px;
  border:3px solid var(--gold);background:rgba(253,250,243,.93)}
.frame::after{content:"";position:absolute;inset:6px;border:1px solid var(--gold-light)}
.ribbon{position:absolute;right:0;top:0;width:170px;height:170px}
.title{position:absolute;top:58px;left:0;right:0;text-align:center;
  font-family:"Noto Serif JP",serif;font-weight:900;font-size:56px;letter-spacing:4px;color:var(--brown)}
.photo{position:absolute}
.photo--party{left:150px;top:150px;width:660px;height:410px;
  background:linear-gradient(135deg,#2c1d12 0%,#6b4524 35%,#c99863 60%,#f2e2c4 80%,#8b5a30 100%)}
.photo--wine{left:20px;top:540px;width:250px;height:250px;border-radius:50%;
  border:4px solid var(--gold);
  background:radial-gradient(circle at 45% 40%,#e9d5a8 0%,#8c6a3a 45%,#2e1f14 90%)}
.photo--interior{left:596px;top:910px;width:226px;height:240px;border-radius:22px;
  border:4px solid var(--gold);
  background:linear-gradient(160deg,#cfe4ef 0%,#9fb5bf 35%,#b04a42 65%,#5a2e24 100%)}
.menu{position:absolute;left:290px;top:585px;width:300px;font-size:17px;line-height:1.5;color:var(--ink)}
.menu__item{margin-bottom:8px}
.menu__head{font-weight:700;font-size:21px}
.menu__head::before{content:"●";color:var(--brown);margin-right:6px;font-size:17px}
.menu__head small{font-size:14px;font-weight:500}
.menu__line{padding-left:24px}
.menu__note{font-size:14px;line-height:1.6;color:var(--ink-soft)}
.brand{position:absolute;left:300px;top:900px;width:280px;text-align:center;
  font-family:"Noto Serif JP",serif;color:var(--brown)}
.brand__mark{width:40px;height:40px;border-radius:50%;background:var(--brown);margin:0 auto 8px}
.brand__name{font-size:24px;font-weight:700;letter-spacing:2px;white-space:nowrap}
.address{position:absolute;left:300px;top:992px;width:280px;font-size:13px;line-height:1.65;
  color:var(--ink);text-align:center;font-style:normal;white-space:nowrap}
</style>
</head>
<body>
<main class="flyer">
  <div class="glitter glitter--top"></div>
  <div class="glitter glitter--right"></div>
  <div class="glitter glitter--bottom"></div>
  <div class="frame"></div>
  <svg class="ribbon" viewBox="0 0 170 170" aria-hidden="true">
    <defs><linearGradient id="rb" x1="0" y1="0" x2="1" y2="1">
      <stop offset="0" stop-color="#f3dc9c"/><stop offset=".5" stop-color="#c9962f"/><stop offset="1" stop-color="#f0d38a"/></linearGradient></defs>
    <polygon points="60,0 100,0 170,70 170,110" fill="url(#rb)"/>
  </svg>

  <h1 class="title">各種パーティー承ります</h1>

  <div class="photo photo--party" role="img" aria-label="ワインで乾杯する料理が並んだパーティーテーブルの写真"></div>
  <div class="photo photo--wine" role="img" aria-label="ワインボトルとグラスの写真"></div>

  <section class="menu">
    <div class="menu__item">
      <p class="menu__head">パーティー <small>（ブッフェ+free drink）</small></p>
      <p class="menu__line">お一人様3,000円, 5,000円, 1万円〜</p>
    </div>
    <div class="menu__item">
      <p class="menu__head">貸切　15万円〜</p>
      <p class="menu__line">30名様以上で2時間から承ります<br>30分ごとに追加料金（1万円）</p>
    </div>
    <div class="menu__item">
      <p class="menu__head">カラオケ <small>（お一人様・1時間当たり）</small></p>
      <p class="menu__line">大ルーム7,000円<br>小ルーム5,000円</p>
    </div>
    <p class="menu__note">※予算・内容に応じてご予約承ります<br>※ディナーご利用時1ドリンクサービス</p>
  </section>

  <div class="brand">
    <div class="brand__mark"></div>
    <p class="brand__name">KAEDE NOGIZAKAA</p>
  </div>

  <address class="address">
    東京都港区北青山5-27-9<br>
    ルミエスホテル&amp;スイート〈青山駅北〉1階<br>
    TEL/FAX　03-6781-2294
  </address>

  <div class="photo photo--interior" role="img" aria-label="赤い椅子が並ぶ明るい店内の写真"></div>
</main>
</body>
</html>
```